Design für Eisverpackung
Zielgruppe
Wir sind ein kleiner regionaler Eisproduzent, betreiben ein Eiscafe mit eigener Produktion. Wir füllen unsere Produkte in Plaste- bzw. Hartpapierbechern ab und vermarkten sie im Einzelhandel, Tankstellen und zu Festen aller Art. Wir benötigen für eine neue Eisverpackung ein ansprechendes und modernes Design.
Aufgabenstellung
Bei der neuen Verpackungseinheit handelt es sich um einen 130ml Hartpapierbecher (Foto Anhang).
Die Designgestaltung umfasst den Becher und ein Rundetikett, welches auf den Becherdeckel platziert wird. Der Becherdeckel selber bleibt neutral weiß,er soll nur mit dem Rundetikett (Durchmesser ca. 6cm) beklebt werden. Eine Skizze als Designvorlage (Becher) finden Sie im Anhang unten. Das Design soll ein hochwertiges Produkt wieder spiegeln.
Bei der Gestaltung des Bechers haben wir schon konkrete Vorstellungen. Der Becher sollte Eissorten-neutral gestaltet werden, da er bei der Verpackung verschiedener Geschmacksrichtungen Anwendung findet.
Des weiteren die Einarbeitung unseres Logo´s (Anhang), der Name des Produktes ("Süßer Moment")und die Bezeichnung Milcheis. Farblich soll der Becher die Farben Hellblau als Grundfarbe und Gelb haben. Der Name " Süßer Moment" vielleicht in rot.
Es müssen auf der Becherrückseite Freiflächen berücksichtigt werden, auf denen wir Informationen wie Inhaltsstoffe und Nährwerte etc. platzieren können.
Die Deckelgestaltung soll im Design natürlich harmonisch zum Gesamtbecher passen.
Zu berücksichtigen ist lediglich, das auf dem Deckel eine Freifläche vorhanden seien muss,
auf der die entsprechende Eissorte Platz findet. Diese wird von uns per Thermodruck entsprechend auf das Deckeletikett platziert.

```html
<!DOCTYPE html>
<html lang="de">
<head>
<meta charset="utf-8">
<title>Süßer Moment – Milcheis Becher und Deckeletikett</title>
<link href="https://fonts.googleapis.com/css2?family=Amatic+SC:wght@400;700&family=Archivo+Black&family=Montserrat:wght@300&display=swap" rel="stylesheet">
<style>
  :root {
    --backdrop: #eef2f0;
    --mint-light: #5fdcc0;
    --mint-deep: #2a8a74;
    --sand-light: #ecd7a4;
    --sand-deep: #d6b67a;
    --ink: #3a3a3a;
    --bar: #2b2b2b;
    --paper: #ffffff;
  }
  * { margin: 0; padding: 0; box-sizing: border-box; }
  html, body { width: 1200px; height: 960px; overflow: hidden; }
  body {
    background: var(--backdrop);
    display: flex;
    align-items: center;
    justify-content: center;
    gap: 70px;
    font-family: "Amatic SC", cursive;
    color: var(--ink);
  }

  /* Round lid label */
  .lid-label {
    position: relative;
    width: 420px;
    height: 420px;
    border-radius: 50%;
    overflow: hidden;
    background: var(--sand-light);
  }
  .lid-label .wave-field {
    position: absolute; inset: 0;
    background: linear-gradient(180deg, var(--sand-light), var(--sand-deep));
  }
  .lid-label .centre-strip {
    position: absolute; top: 0; bottom: 0; left: 88px; width: 244px;
    background: linear-gradient(160deg, var(--mint-light), var(--mint-deep));
    display: flex; flex-direction: column; align-items: center;
    padding-top: 38px;
  }
  .brand {
    display: flex; align-items: center; gap: 8px;
    font-family: "Amatic SC", cursive; font-weight: 700;
    color: var(--ink);
  }
  .brand .dot { border-radius: 50%; background: var(--paper); }
  .lid-label .brand { font-size: 30px; }
  .lid-label .brand .dot { width: 14px; height: 14px; }
  .lid-label .tagline { font-size: 9px; margin-top: 2px; }
  .lid-label .product-name { margin-top: 14px; }
  .lid-label .product-name .small { font-size: 34px; }
  .lid-label .product-name .large { font-size: 70px; }
  .flavour-bar {
    position: absolute; left: 40px; right: 40px; top: 252px; height: 56px;
    background: var(--bar); border-radius: 4px;
    display: flex; align-items: center; justify-content: center;
    font-family: "Archivo Black", sans-serif; font-size: 34px;
    letter-spacing: 2px; color: var(--paper);
  }

  /* Cup wrap front */
  .cup-wrap {
    position: relative;
    width: 560px;
    height: 720px;
    background: linear-gradient(180deg, var(--sand-light), var(--sand-deep));
  }
  .cup-wrap .front-panel {
    position: absolute; top: 0; bottom: 0; left: 120px; right: 120px;
    background: linear-gradient(165deg, var(--mint-light), var(--mint-deep));
    display: flex; flex-direction: column; align-items: center;
    padding-top: 36px;
  }
  .category {
    font-family: "Amatic SC", cursive; font-size: 36px;
    letter-spacing: 22px; padding-left: 22px;
  }
  .product-name {
    display: flex; flex-direction: column; align-items: center;
    line-height: 0.85; text-transform: uppercase;
  }
  .cup-wrap .product-name { margin-top: 110px; }
  .cup-wrap .product-name .small { font-size: 60px; }
  .cup-wrap .product-name .large { font-size: 130px; }
  .cup-wrap .brand-block {
    margin-top: auto; margin-bottom: 40px;
    display: flex; flex-direction: column; align-items: center;
  }
  .cup-wrap .brand { font-size: 48px; }
  .cup-wrap .brand .dot { width: 22px; height: 22px; }
  .tagline {
    font-family: "Montserrat", sans-serif; font-weight: 300;
    font-size: 13px; letter-spacing: 2px;
  }
</style>
</head>
<body>
  <section class="lid-label" aria-label="Deckeletikett">
    <div class="wave-field" role="img" aria-label="Wellenmuster in Sandgelb"></div>
    <div class="centre-strip">
      <div class="brand"><span class="dot"></span>Talhofer</div>
      <div class="tagline">natürlich lecker!</div>
      <div class="product-name">
        <span class="small">Süßer</span>
        <span class="large">Moment</span>
      </div>
    </div>
    <div class="flavour-bar">EISSORTE</div>
  </section>

  <section class="cup-wrap" aria-label="Becher Vorderseite">
    <div class="wave-field" role="img" aria-label="Wellenmuster in Sandgelb an den Seiten"></div>
    <div class="front-panel">
      <div class="category">MILCHEIS</div>
      <div class="product-name">
        <span class="small">Süßer</span>
        <span class="large">Moment</span>
      </div>
      <div class="brand-block">
        <div class="brand"><span class="dot"></span>Talhofer</div>
        <div class="tagline">natürlich lecker!</div>
      </div>
    </div>
  </section>
</body>
</html>
```